Business Card Design

We need a business card design for our new expansion based in Bloomfield Hills, Michigan. Our company is Quiet Harbor Institute & Wellness Center. Our Academy teaches individuals of all ages and professions to live from their soul. We teach intuitive development, meditation and mindfulness; shamanic healing. And ourr healing center provides holistic services. We offer certification programs that support the ethical practices of Intuitive professionals. Our team of Intuitive Practitioners includes: doctors, psychologists, chiropractor, soul retrievers, mediums, etc who all balance their knowledge with intuitive wisdom.

We want our symbol to be the Blue Morpho Buttefly and the colors on the card to complement it. We want to communicate inspiration, healing and empowerment. Thank you

Industry/Entity Type

Business

Contact Information for Business Card

Dana Farrow
Medium. Author. Soul Retriever.
Founder, Quiet Harbor

Quiet Harbor

19 East Cedar Mill Drive Suite 200
Maple Ridge, OH 44391
614-555-0174

www.danafarrowexample.com

Requirements
Must have
• blue morpho butterfly

```html
<!DOCTYPE html>
<html lang="en">
<head>
<meta charset="utf-8">
<title>Quiet Harbor – Business Card</title>
<link rel="stylesheet" href="https://fonts.googleapis.com/css2?family=Arimo:ital,wght@0,400;1,400&display=swap">
<style>
  :root {
    --page: #e9e9eb;
    --ink-black: #050505;
    --morpho-blue: #2f8fdc;
    --morpho-light: #4fb3ee;
    --band-deep: #1d5fb8;
    --paper: #f4f4f5;
    --text-dark: #111111;
    --text-light: #ffffff;
  }
  html, body {
    margin: 0;
    padding: 0;
    width: 1200px;
    height: 873px;
    overflow: hidden;
    background: var(--page);
    font-family: "Arimo", Arial, sans-serif;
  }
  .canvas {
    position: relative;
    width: 1200px;
    height: 873px;
  }
  .card {
    position: absolute;
    overflow: hidden;
    box-shadow: 0 6px 18px rgba(0,0,0,0.25);
  }
  .card svg { position: absolute; inset: 0; display: block; }

  /* Back of card – landscape */
  .card-back {
    left: 55px;
    top: 395px;
    width: 660px;
    height: 371px;
    background: var(--ink-black);
  }
  .card-back .website {
    position: absolute;
    right: 36px;
    bottom: 26px;
    margin: 0;
    font-style: italic;
    font-size: 15px;
    color: var(--morpho-light);
  }

  /* Front of card – portrait */
  .card-front {
    left: 775px;
    top: 106px;
    width: 371px;
    height: 660px;
    background: var(--paper);
  }
  .identity {
    position: absolute;
    top: 88px;
    left: 0;
    width: 100%;
    text-align: center;
    font-style: italic;
    padding-left: 30px;
    box-sizing: border-box;
  }
  .identity .name {
    margin: 0 0 8px;
    font-size: 30px;
    font-weight: 400;
    color: var(--text-light);
  }
  .identity .roles {
    list-style: none;
    margin: 0;
    padding: 0;
    font-size: 19px;
    line-height: 24px;
    color: var(--morpho-light);
  }
  .contact {
    position: absolute;
    top: 428px;
    left: 0;
    width: 100%;
    padding-left: 20px;
    box-sizing: border-box;
    text-align: center;
    font-style: italic;
    font-size: 18px;
    line-height: 24px;
    color: var(--text-dark);
  }
  .contact p { margin: 0 0 22px; }
</style>
</head>
<body>
<main class="canvas">

  <section class="card card-back" aria-label="Card back">
    <svg width="660" height="371" viewBox="0 0 660 371">
      <defs>
        <linearGradient id="morphoPhoto" x1="0" y1="0" x2="1" y2="1">
          <stop offset="0" stop-color="#1f3b22"/>
          <stop offset="0.35" stop-color="#3aa6e6"/>
          <stop offset="0.6" stop-color="#7fcaf5"/>
          <stop offset="1" stop-color="#173120"/>
        </linearGradient>
      </defs>
      <path role="img" aria-label="Photograph of a blue morpho butterfly resting on pink flowers among green leaves"
            d="M0,0 H440 C520,90 500,250 330,371 H0 Z" fill="url(#morphoPhoto)"/>
      <path d="M440,0 C520,90 500,250 330,371" fill="none" stroke="var(--band-deep)" stroke-width="16"/>
      <path d="M452,0 C532,90 512,250 342,371" fill="none" stroke="var(--morpho-blue)" stroke-width="6"/>
    </svg>
    <p class="website">www.danafarrowexample.com</p>
  </section>

  <section class="card card-front" aria-label="Card front">
    <svg width="371" height="660" viewBox="0 0 371 660">
      <defs>
        <radialGradient id="faintWing" cx="0.5" cy="0.6" r="0.6">
          <stop offset="0" stop-color="#c9cacc"/>
          <stop offset="1" stop-color="#f4f4f5"/>
        </radialGradient>
      </defs>
      <rect role="img" aria-label="Faint grey image of a morpho butterfly behind the contact details"
            x="0" y="260" width="371" height="400" fill="url(#faintWing)"/>
      <path d="M0,0 H371 V395 C300,330 150,270 0,268 Z" fill="var(--ink-black)"/>
      <path d="M0,272 C150,274 300,334 371,399" fill="none" stroke="var(--band-deep)" stroke-width="9"/>
      <path d="M0,280 C150,282 300,342 371,407" fill="none" stroke="var(--morpho-blue)" stroke-width="4"/>
    </svg>
    <div class="identity">
      <h1 class="name">Dana Farrow</h1>
      <ul class="roles">
        <li>Medium</li>
        <li>Author</li>
        <li>Soul Retriever</li>
        <li>Founder</li>
      </ul>
    </div>
    <div class="contact">
      <p>Quiet Harbor<br>19 East Cedar Mill Drive<br>Suite 200<br>Maple Ridge, OH 44391</p>
      <p>614-555-0174<br>www.danafarrowexample.com</p>
    </div>
  </section>

</main>
</body>
</html>
```